Dryer Vent Cleaning Postcard Design

We need a postcard design for Flue Wranglers, a company that specializes in dryer vent cleaning, repairs and upgrades. Dryer vents need periodic cleaning to avoid lint clogging, dryer malfunction, long dry times and even a house fire. This card will be sent to residential and businesses prospects to introduce them to our services and the importance of maintaining their dryer vents. Our website is @ fluewrangling.com and provides information about our services, photos of our work and our general color scheme (purple/orange). Final print size will be 5x7 horizontal.

Target Market(s)

homeowners and business owners (spas, salons, grooming, gyms, laundrymats, etc)

Requirements
Must have
• Reduce the risk of fire
shortened dry times
lower energy consumption
18000 dryer fires caused in the US per year
Nice to have
• Does your dryer take too long to dry?

```html
<!DOCTYPE html>
<html lang="en">
<head>
<meta charset="utf-8">
<title>Flue Wranglers – Dryer Vent Postcard</title>
<link rel="stylesheet" href="https://fonts.googleapis.com/css2?family=Anton&family=Oswald:wght@600&family=Montserrat:wght@300;700;800&display=swap">
<style>
  :root {
    --orange: #ec4a2f;
    --purple: #4a3a7c;
    --white: #ffffff;
    --backdrop: #2b2b2b;
    --line: #222222;
  }
  * { box-sizing: border-box; margin: 0; padding: 0; }
  html, body { width: 1200px; height: 1000px; overflow: hidden; }
  body {
    background: var(--backdrop);
    font-family: "Montserrat", sans-serif;
    position: relative;
  }
  .card {
    position: absolute;
    left: 285px;
    width: 630px;
    height: 450px;
    background: var(--white);
    overflow: hidden;
    box-shadow: 0 8px 24px rgba(0,0,0,.45);
  }
  .card--front { top: 40px; }
  .card--back { top: 510px; }
  .card__shapes { position: absolute; inset: 0; }

  .brand {
    position: absolute;
    display: flex;
    align-items: center;
    gap: 8px;
    font-weight: 800;
    color: var(--purple);
    text-transform: uppercase;
    letter-spacing: .5px;
    white-space: nowrap;
  }
  .brand__dot {
    width: 14px; height: 14px; border-radius: 50%;
    background: var(--orange);
  }
  .card--front .brand { left: 32px; top: 48px; font-size: 17px; }
  .card--back .brand { right: 60px; top: 268px; font-size: 13px; }

  .art { position: absolute; border-radius: 6px; }
  .art--dryer-tech {
    left: 350px; top: 40px; width: 255px; height: 380px;
    background: linear-gradient(135deg, #d8d5d2 0%, #b9a48e 45%, #c9262a 100%);
    opacity: .9;
  }
  .art--vent-tech {
    left: 40px; top: 232px; width: 200px; height: 208px;
    background: linear-gradient(160deg, #a08b78 0%, #4a5aa6 60%, #3c2f7a 100%);
    opacity: .85;
  }

  .headline-lead {
    position: absolute; left: 30px; top: 152px;
    font-family: "Oswald", sans-serif; font-weight: 600;
    font-size: 20px; color: var(--purple); letter-spacing: -.3px;
    text-transform: uppercase; white-space: nowrap;
  }
  .headline-big {
    position: absolute; left: 28px; top: 170px;
    font-family: "Anton", sans-serif; font-size: 118px; line-height: 1;
    color: var(--orange);
  }
  .pill {
    position: absolute; left: 0; top: 305px;
    width: 335px; height: 40px;
    background: var(--purple); color: var(--white);
    border-radius: 0 20px 20px 0;
    font-weight: 800; font-size: 19px;
    display: flex; align-items: center; padding-left: 30px;
    text-transform: uppercase; white-space: nowrap;
  }
  .risk {
    position: absolute; left: 32px; top: 358px;
    color: var(--purple); text-transform: uppercase;
    font-weight: 300; font-size: 26px; line-height: 1;
  }
  .risk strong {
    display: block; color: var(--orange); font-weight: 800; font-size: 34px; margin-top: 2px;
  }

  .stamp {
    position: absolute; right: 80px; top: 36px;
    width: 78px; height: 62px; border: 1.5px solid var(--line);
  }
  .address-lines { position: absolute; right: 40px; top: 112px; width: 205px; }
  .address-lines span { display: block; height: 34px; border-bottom: 1.5px solid var(--line); }

  .stat {
    position: absolute; left: 180px; top: 128px;
    color: var(--purple); text-transform: uppercase; line-height: 1.08;
    font-size: 20px; white-space: nowrap;
  }
  .stat__num { color: var(--orange); font-weight: 800; }
  .stat__bold { font-weight: 800; }
  .stat__light { font-weight: 300; }

  .energy {
    position: absolute; left: 262px; top: 312px;
    text-transform: uppercase; font-weight: 800; font-size: 26px; line-height: 1.08;
    color: var(--purple); white-space: nowrap;
  }
  .energy__accent { color: var(--orange); }
</style>
</head>
<body>

<section class="card card--front" aria-label="Postcard front">
  <svg class="card__shapes" viewBox="0 0 630 450" aria-hidden="true">
    <path d="M290 0 H630 V450 H345 C285 400 300 330 360 290 C420 250 400 80 290 0 Z" fill="var(--orange)"/>
    <path d="M255 0 C370 40 420 150 395 255 C385 170 330 60 255 0 Z" fill="var(--purple)"/>
    <path d="M345 450 C300 410 300 350 345 320 C325 360 330 410 370 450 Z" fill="var(--purple)"/>
  </svg>
  <div class="brand"><span class="brand__dot"></span>Flue Wranglers</div>
  <div class="art art--dryer-tech" role="img" aria-label="Illustration of a technician with a red vent cleaning machine beside a clothes dryer overflowing with lint"></div>
  <p class="headline-lead">Does your dryer take too long to</p>
  <p class="headline-big">DRY?</p>
  <p class="pill">Shortened dry times</p>
  <p class="risk">Reduce<br>the risk of<strong>Fire</strong></p>
</section>

<section class="card card--back" aria-label="Postcard back">
  <svg class="card__shapes" viewBox="0 0 630 450" aria-hidden="true">
    <rect width="630" height="450" fill="var(--orange)"/>
    <ellipse cx="420" cy="275" rx="430" ry="295" fill="var(--white)"/>
    <path d="M120 445 C20 330 60 120 230 55 C120 140 80 300 150 445 Z" fill="var(--purple)"/>
    <path d="M560 145 C620 230 610 340 560 410 C590 330 590 230 560 145 Z" fill="var(--purple)"/>
  </svg>
  <div class="stamp"></div>
  <div class="address-lines"><span></span><span></span><span></span><span></span></div>
  <p class="stat">
    <span class="stat__num">18000</span><br>
    <span class="stat__bold">Dryer fires</span><br>
    <span class="stat__light">Caused in the</span><br>
    <span class="stat__bold">US per year</span>
  </p>
  <div class="art art--vent-tech" role="img" aria-label="Illustration of a smiling technician holding a vent brush with a coiled hose"></div>
  <p class="energy">Lower<br><span class="energy__accent">Energy</span><br>Consumption</p>
  <div class="brand"><span class="brand__dot"></span>Flue Wranglers</div>
</section>

</body>
</html>
```